Record Label Needs Design for CD Case, Booklet, and CD...

We are a christian record label looking to make a difference in this world.

We need 3 files -
The front and back of CD case and the actual CD graphics.

It is entitled

"Larkspan Records and Friends Summer Sampler 2014"

We will give you the artists and songs on the CD.

Please send IDEAS WE ARE OPEN TO ANYTHING!!!

you can find information on our record label at www.larkspanrecords.net or www.facebook.com/larkspanrecords

The 2 artists on the summer sampler are Ferncastle - and Paper Harbor

I have pictures of Ferncastle attached below, and pictures of paper harbor below...

ferncastlepraise.net has their logo
paper harbors logo is attached...

This is a guaranteed payout and Ive had much luck with pixel bazaar. Looking forward to another successful contest.

martin@larkspanrecords.net

Reason: We haven't had any responses yet so we extended this out a few days!

Reason: We need better designs...

Come on guys!  Send in some new designs!  I am not hard to please!  I just updated the color schemes, etc....

Target Market(s)

Christians

Industry/Entity Type

Artists

Colors
d3a5cc
ed9dc4
8768ae

Requirements
Must have
• Positivity
Nice to have
• Doves are nice
Should not have
• Crosses

```html
<!DOCTYPE html>
<html lang="en">
<head>
<meta charset="utf-8">
<title>Larkspan Records – Summer Sampler 2014 – Back Cover</title>
<link rel="stylesheet" href="https://fonts.googleapis.com/css2?family=Tinos&family=Josefin+Sans:wght@700&display=swap">
<style>
  :root {
    --page: #ffffff;
    --ink: #000000;
    --cream: #fdf6c4;
    --amber-deep: #ef7d22;
    --amber: #f8a92a;
    --sun: #f4e93a;
    --sun-pale: #f6f06a;
  }
  * { margin: 0; padding: 0; box-sizing: border-box; }
  html, body {
    width: 1200px; height: 1000px; overflow: hidden;
    background: var(--page);
  }
  .canvas { position: relative; width: 1200px; height: 1000px; }

  .side-label {
    position: absolute; left: 0; width: 1100px; top: 38px;
    text-align: center;
    font-family: "Tinos", "Times New Roman", serif;
    font-size: 92px; font-weight: 400; letter-spacing: 1px;
    color: var(--ink); line-height: 1;
  }

  .back-cover {
    position: absolute; left: 236px; top: 161px;
    width: 738px; height: 801px;
    background: var(--cream);
    border: 2px solid var(--ink);
    overflow: hidden;
  }
  .facet-field { position: absolute; left: 0; top: 0; width: 734px; height: 797px; }
  .inner-frame {
    position: absolute; left: 18px; top: 20px;
    width: 701px; height: 762px;
    border: 1.5px solid var(--ink);
  }

  .track-list {
    position: absolute; left: 42px; top: 111px;
    list-style: none;
    font-family: "Josefin Sans", "Arial", sans-serif;
    font-weight: 700; font-variant: small-caps;
    font-size: 22px; line-height: 30px; color: var(--ink);
  }

  .label-mark {
    position: absolute; left: 32px; top: 506px;
    display: flex; align-items: center; gap: 10px;
    font-family: "Tinos", "Times New Roman", serif;
    font-size: 22px; color: var(--ink);
  }
  .label-mark .mark-square { width: 18px; height: 18px; background: var(--ink); }

  .imprint {
    position: absolute; left: 35px; top: 582px;
    font-family: "Tinos", "Times New Roman", serif;
    font-size: 16.5px; line-height: 22.5px; color: var(--ink);
  }
  .imprint .credits { margin-top: 23px; }
</style>
</head>
<body>
<div class="canvas">
  <h1 class="side-label">BACK</h1>

  <section class="back-cover">
    <svg class="facet-field" viewBox="0 0 734 797" role="img" aria-label="Geometric pattern of orange and yellow triangles along the right side">
      <defs>
        <linearGradient id="facetTone" x1="0" y1="0" x2="0" y2="1">
          <stop offset="0" stop-color="var(--amber-deep)"/>
          <stop offset="0.2" stop-color="var(--amber)"/>
          <stop offset="0.45" stop-color="var(--sun)"/>
          <stop offset="0.7" stop-color="var(--sun-pale)"/>
          <stop offset="1" stop-color="var(--amber)"/>
        </linearGradient>
      </defs>
      <polygon fill="url(#facetTone)" opacity="0.9"
        points="349,74 380,0 734,0 734,797 480,797 390,730 430,660 350,590 390,520 350,440 390,380 430,300 350,225 390,150"/>
    </svg>

    <div class="inner-frame"></div>

    <ol class="track-list">
      <li>1. Track List</li>
      <li>2. Track List</li>
      <li>3. Track List</li>
      <li>4. Track List</li>
      <li>5. Track List</li>
      <li>6. Track List</li>
      <li>7. Track List</li>
      <li>8. Track List</li>
      <li>9. Track List</li>
    </ol>

    <div class="label-mark">
      <span class="mark-square"></span>
      <span class="mark-name">Larkspan Records</span>
    </div>

    <div class="imprint">
      <p class="links">©2014 Larkspan Records,<br>www.larkspanrecords.net<br>www.facebook.com/larkspanrecords</p>
      <p class="credits">catalog number,<br>contact info,<br>production credits,<br>Producer’s name, more</p>
    </div>
  </section>
</div>
</body>
</html>
```